Brightmoor Surface Index

I have a current web site that it looking quite aged and it needs a new lease of life. This is a Graffiti Management Website so is all about data processing and management of information. I want a html 5 view on any platform design. clean crisp and new. I have provided some screen shots of my current site.

Target Market(s)

The Target Market will be local government. most users will not be heavy pc users

Industry/Entity Type

Management

Font styles to use
Sans Serif
Other font styles liked:
• web font like calibri

Colors

Designer to choose colors to be used in the design.

Requirements
Must have
• Must have menus similar to attachments

```html
<!DOCTYPE html>
<html lang="en">
<head>
<meta charset="utf-8">
<title>Brightmoor Surface Index</title>
<link rel="stylesheet" href="https://fonts.googleapis.com/css2?family=Open+Sans:wght@400;600;700&family=Carlito:wght@400;700&display=swap">
<style>
  :root {
    --green: #8dc63f;
    --green-dark: #5f9a1c;
    --ink: #1a1a1a;
    --concrete: #dcdad6;
    --concrete-light: #e6e4e0;
    --footer: #111111;
    --footer-line: #2c2c2c;
    --footer-text: #d4d4d4;
    --white: #ffffff;
  }
  * { margin: 0; padding: 0; box-sizing: border-box; }
  html, body { width: 1200px; height: 800px; overflow: hidden; }
  body {
    position: relative;
    font-family: "Carlito", "Open Sans", sans-serif;
    color: var(--ink);
    background: var(--concrete);
  }

  .site-header {
    position: absolute; left: 0; top: 0; width: 1200px; height: 48px;
    background: linear-gradient(#e9e7e3, #d8d6d2);
    border-bottom: 3px solid #2a2a2a;
  }
  .brand {
    position: absolute; left: 185px; top: 0; width: 157px; height: 48px;
    background: var(--green);
    display: flex; align-items: center; justify-content: center;
    font-family: "Open Sans", sans-serif; font-weight: 700;
    font-size: 24px; letter-spacing: 3px; color: var(--ink);
  }
  .main-nav a {
    position: absolute; top: 21px;
    font-family: "Open Sans", sans-serif; font-weight: 700; font-size: 12px;
    color: #222; text-decoration: none; line-height: 14px;
  }
  .main-nav a.is-active { color: var(--green-dark); }
  .main-nav .divider {
    position: absolute; top: 20px; width: 1px; height: 15px; background: #777;
  }

  .hero {
    position: absolute; left: 0; top: 51px; width: 1200px; height: 226px;
    background:
      radial-gradient(ellipse 200px 180px at 50% 85%, #1c1c1c 0%, rgba(28,28,28,0) 100%),
      linear-gradient(100deg, #2a2a2a 0%, #6a6a6a 25%, #8c8c8c 45%, #5c5c5c 65%, #9a9a9a 82%, #3a3a3a 100%);
  }
  .hero-title {
    position: absolute; left: 0; top: 48px; width: 1200px; text-align: center;
    font-family: "Open Sans", sans-serif; font-weight: 400; font-size: 40px;
    color: var(--white); letter-spacing: 0.5px;
    text-shadow: 0 3px 6px rgba(0,0,0,0.7);
  }

  .features {
    position: absolute; left: 0; top: 277px; width: 1200px; height: 325px;
    background: radial-gradient(ellipse at 50% 40%, var(--concrete-light), var(--concrete));
  }
  .feature {
    position: absolute; top: 42px; width: 170px; text-align: center;
  }
  .feature svg { display: block; margin: 0 auto; width: 80px; height: 80px; }
  .feature p {
    margin-top: 38px; font-size: 12.5px; line-height: 15.4px; color: #1d1d1d;
  }

  .site-footer {
    position: absolute; left: 0; top: 602px; width: 1200px; height: 198px;
    background: var(--footer); border-top: 3px solid var(--green);
  }
  .footer-heading {
    position: absolute; top: 28px;
    font-family: "Open Sans", sans-serif; font-weight: 700; font-size: 11px;
    color: var(--white);
  }
  .legislation-list { position: absolute; left: 191px; top: 53px; list-style: none; }
  .legislation-list li {
    position: relative; padding-left: 15px; height: 21px;
    font-family: "Open Sans", sans-serif; font-size: 11px; color: var(--footer-text);
  }
  .legislation-list li::before {
    content: ""; position: absolute; left: 1px; top: 3px;
    border-left: 5px solid var(--green);
    border-top: 4px solid transparent; border-bottom: 4px solid transparent;
  }
  .contact-list {
    position: absolute; left: 659px; top: 53px;
    display: grid; grid-template-columns: 78px auto; row-gap: 0;
    font-family: "Open Sans", sans-serif; font-size: 11px; line-height: 14.5px;
  }
  .contact-list dt { color: var(--green); font-weight: 600; }
  .contact-list dd { color: var(--footer-text); }
  .copyright {
    position: absolute; left: 0; top: 155px; width: 1200px; height: 43px;
    border-top: 1px solid var(--footer-line);
    text-align: center; line-height: 40px;
    font-family: "Open Sans", sans-serif; font-size: 11.5px; color: var(--white);
  }
</style>
</head>
<body>

<header class="site-header">
  <div class="brand">BMSI</div>
  <nav class="main-nav">
    <a class="is-active" href="#" style="left:409px">USER HOME</a>
    <span class="divider" style="left:491px"></span>
    <a href="#" style="left:502px">ADD A JOB</a>
    <span class="divider" style="left:569px"></span>
    <a href="#" style="left:580px">CURRENT JOBS</a>
    <span class="divider" style="left:669px"></span>
    <a href="#" style="left:682px">SEARCH JOBS</a>
    <span class="divider" style="left:765px"></span>
    <a href="#" style="left:783px">REPORTS</a>
    <span class="divider" style="left:846px"></span>
    <a href="#" style="left:861px">USER DETAILS</a>
    <span class="divider" style="left:949px"></span>
    <a href="#" style="left:961px">ADMIN</a>
  </nav>
</header>

<section class="hero" role="img" aria-label="Black and white photo of an artist drawing a large mural on a wall">
  <h1 class="hero-title">HELPING YOU CLEAN UP YOUR COMMUNITY</h1>
</section>

<section class="features">
  <div class="feature" style="left:193px">
    <svg viewBox="0 0 80 80" aria-hidden="true">
      <g fill="#8dc63f">
        <circle cx="26" cy="22" r="14"/>
        <rect x="23" y="4" width="6" height="36"/>
        <rect x="8" y="19" width="36" height="6"/>
        <rect x="23" y="4" width="6" height="36" transform="rotate(45 26 22)"/>
        <rect x="23" y="4" width="6" height="36" transform="rotate(-45 26 22)"/>
      </g>
      <circle cx="26" cy="22" r="5" fill="#dcdad6"/>
      <g fill="#1a1a1a">
        <circle cx="58" cy="42" r="12"/>
        <rect x="55" y="27" width="6" height="30"/>
        <rect x="43" y="39" width="30" height="6"/>
        <rect x="55" y="27" width="6" height="30" transform="rotate(45 58 42)"/>
        <rect x="55" y="27" width="6" height="30" transform="rotate(-45 58 42)"/>
        <circle cx="22" cy="60" r="10"/>
        <rect x="19" y="47" width="6" height="26"/>
        <rect x="9" y="57" width="26" height="6"/>
        <rect x="19" y="47" width="6" height="26" transform="rotate(45 22 60)"/>
        <rect x="19" y="47" width="6" height="26" transform="rotate(-45 22 60)"/>
      </g>
      <circle cx="58" cy="42" r="4.5" fill="#dcdad6"/>
      <circle cx="22" cy="60" r="3.5" fill="#dcdad6"/>
    </svg>
    <p>BMSI is an Online Database System to Manage Graffiti in your area or Your Properties. BMSI allows you to Register, Track, Report and Archive Graffiti Jobs with Photographic Records.</p>
  </div>

  <div class="feature" style="left:402px">
    <svg viewBox="0 0 80 80" aria-hidden="true">
      <rect x="20" y="10" width="52" height="48" fill="#1a1a1a" transform="rotate(10 46 34)"/>
      <rect x="10" y="18" width="56" height="52" fill="#1a1a1a"/>
      <rect x="16" y="24" width="44" height="40" fill="#8dc63f"/>
      <g stroke="#fff" stroke-width="2.5" fill="#fff">
        <line x1="30" y1="44" x2="46" y2="35"/>
        <line x1="30" y1="44" x2="46" y2="53"/>
        <circle cx="30" cy="44" r="4"/>
        <circle cx="46" cy="35" r="4"/>
        <circle cx="46" cy="53" r="4"/>
      </g>
    </svg>
    <p>BMSI records both Estimated and Actual hours and costs for each job, enabling you to track the effectiveness of Anti Graffiti policy.</p>
  </div>

  <div class="feature" style="left:611px">
    <svg viewBox="0 0 80 80" aria-hidden="true">
      <path d="M12 6 H48 L60 18 V74 H12 Z" fill="#fff" stroke="#1a1a1a" stroke-width="4"/>
      <path d="M48 6 V18 H60" fill="none" stroke="#1a1a1a" stroke-width="3"/>
      <g stroke="#1a1a1a" stroke-width="3">
        <line x1="20" y1="28" x2="50" y2="28"/>
        <line x1="20" y1="38" x2="50" y2="38"/>
        <line x1="20" y1="48" x2="40" y2="48"/>
        <line x1="20" y1="58" x2="34" y2="58"/>
      </g>
      <path d="M36 66 L40 54 L68 26 L76 34 L48 62 Z" fill="#8dc63f"/>
    </svg>
    <p>BMSI allows sharing of Critical Graffiti Tag and Photographic Data between its subscribers, assisting with tracking down Serial Graffiti Offenders.</p>
  </div>

  <div class="feature" style="left:823px">
    <svg viewBox="0 0 80 80" aria-hidden="true">
      <polyline points="8,30 28,22 46,26 68,12" fill="none" stroke="#8dc63f" stroke-width="3"/>
      <g fill="#8dc63f">
        <circle cx="8" cy="30" r="4"/><circle cx="28" cy="22" r="4"/>
        <circle cx="46" cy="26" r="4"/><circle cx="68" cy="12" r="4"/>
      </g>
      <g fill="#1a1a1a">
        <rect x="4" y="46" width="12" height="28"/>
        <rect x="22" y="38" width="12" height="36"/>
        <rect x="40" y="42" width="12" height="32"/>
        <rect x="58" y="30" width="12" height="44"/>
      </g>
    </svg>
    <p>BMSI has a Statistical and Comparison Reporting Systems to allow its subscribers to graphically report and compare their Graffiti Data.</p>
  </div>
</section>

<footer class="site-footer">
  <h2 class="footer-heading" style="left:191px">LEGISLATION</h2>
  <ul class="legislation-list">
    <li>NSW Graffiti Legislation</li>
    <li>NSW Government Perspective on Graffiti</li>
    <li>NSW Local Government Graffiti Ammendment ACT 2002</li>
    <li>NSW Local Government Legislation Regarding Graffiti Removal</li>
  </ul>

  <h2 class="footer-heading" style="left:659px">CONTACT US</h2>
  <dl class="contact-list">
    <dt>Telephone</dt><dd>Brightmoor Surface Index</dd>
    <dt></dt><dd>PO Box 612, Kellbrook, NSW 2384</dd>
    <dt>Fax</dt><dd>(02) 5550 1823</dd>
    <dt>Email</dt><dd>enquiries@bmsi.example</dd>
    <dt>Support</dt><dd>support@bmsi.example</dd>
  </dl>

  <p class="copyright">Copyright 2014 BMSI all rights reserved</p>
</footer>

</body>
</html>
```